design an extra page for our profile

we are looking for someone to create another page like the attached but with the below changes:
heading changed to (Construction)
icons changed and names to reflect new services i.e
- Residential Building
- Commercial Building
- Landscaping
- Concrete
- Painting

the very bottom of the page is to stay the same with our office info

```html
<!DOCTYPE html>
<html lang="en">
<head>
<meta charset="utf-8">
<title>KARRO – Construction Profile Page</title>
<link rel="stylesheet" href="https://fonts.googleapis.com/css2?family=Montserrat:wght@400;500;600;700&display=swap">
<style>
  :root {
    --brand-navy: #253c91;
    --panel-grey: #e7e7e7;
    --paper: #ffffff;
    --frame-line: #c9c9c9;
    --photo-light: #f1f3f5;
    --photo-mid: #d9dee4;
    --photo-cool: #bfc9cf;
  }
  * { margin: 0; padding: 0; box-sizing: border-box; }
  html, body { width: 1200px; height: 744px; overflow: hidden; background: var(--paper); }
  body {
    position: relative;
    border: 1px solid var(--frame-line);
    font-family: "Montserrat", sans-serif;
  }
  .flyer {
    position: absolute;
    top: 49px;
    width: 500px;
    height: 646.6px;
  }
  .flyer--navy { left: 57px; }
  .flyer--light { left: 650px; }
  .flyer text { font-family: "Montserrat", sans-serif; }

  /* shared parts */
  .photo-area { fill: url(#photoTone); }
  .accent-stripe { fill: none; stroke: var(--brand-navy); stroke-width: 14; }
  .heading-tab { fill: var(--brand-navy); }
  .heading-rule { stroke: var(--brand-navy); stroke-width: 6; }
  .heading-text { fill: var(--paper); font-size: 40px; font-weight: 600; letter-spacing: 0.5px; }
  .city-list { font-size: 21px; font-weight: 500; letter-spacing: 0.3px; }
  .brand-name { font-size: 58px; font-weight: 600; letter-spacing: 1px; }
  .offer-text { font-size: 25px; font-weight: 400; }
  .offer-text tspan.offer-strong { font-weight: 700; }
  .service-box { fill: var(--paper); stroke: var(--brand-navy); stroke-width: 1.5; stroke-opacity: 0.75; }
  .service-icon { color: var(--brand-navy); }
  .service-label { fill: var(--brand-navy); font-size: 19.5px; font-weight: 700; text-anchor: middle; }
  .contact-line { font-size: 26.5px; font-weight: 600; letter-spacing: 0.4px; }
  .footer-brand { font-size: 50px; font-weight: 600; letter-spacing: 1px; }

  /* navy variant */
  .flyer--navy .header-panel,
  .flyer--navy .footer-panel { fill: var(--brand-navy); }
  .flyer--navy .fine-stripe { fill: none; stroke: var(--paper); stroke-width: 4; }
  .flyer--navy .city-list,
  .flyer--navy .brand-name,
  .flyer--navy .footer-brand,
  .flyer--navy .contact-line { fill: var(--paper); }
  .flyer--navy .contact-icon { color: var(--paper); }
  .flyer--navy .offer-pill { fill: var(--paper); stroke: var(--brand-navy); stroke-width: 2; }
  .flyer--navy .offer-text { fill: var(--brand-navy); }
  .flyer--navy .footer-rule { display: none; }

  /* light variant */
  .flyer--light .header-panel,
  .flyer--light .footer-panel { fill: var(--panel-grey); }
  .flyer--light .fine-stripe { fill: none; stroke: var(--brand-navy); stroke-width: 4; }
  .flyer--light .city-list,
  .flyer--light .brand-name,
  .flyer--light .footer-brand,
  .flyer--light .contact-line { fill: var(--brand-navy); }
  .flyer--light .contact-icon { color: var(--brand-navy); }
  .flyer--light .offer-pill { fill: var(--brand-navy); }
  .flyer--light .offer-text { fill: var(--paper); }
  .flyer--light .footer-rule { stroke: var(--brand-navy); stroke-width: 6; }
  .flyer--light .flyer-edge { fill: none; stroke: var(--frame-line); stroke-width: 1.5; }
  .flyer--navy .flyer-edge { display: none; }

  .symbol-library { position: absolute; width: 0; height: 0; overflow: hidden; }
</style>
</head>
<body>

<svg class="symbol-library" aria-hidden="true">
  <defs>
    <linearGradient id="photoTone" x1="0" y1="0" x2="1" y2="1">
      <stop offset="0" stop-color="#e9ecef"/>
      <stop offset="0.45" stop-color="#cfd8de"/>
      <stop offset="0.7" stop-color="#e4e8ec"/>
      <stop offset="1" stop-color="#f3f4f6"/>
    </linearGradient>
    <linearGradient id="tabFade" x1="0" y1="0" x2="1" y2="0">
      <stop offset="0" stop-color="#253c91"/>
      <stop offset="1" stop-color="#253c91" stop-opacity="0"/>
    </linearGradient>

    <symbol id="icon-residential" viewBox="0 0 120 120">
      <rect x="54" y="2" width="64" height="5" fill="currentColor" transform="translate(-28 0)"/>
      <rect x="30" y="10" width="60" height="94" fill="currentColor"/>
      <g fill="#fff">
        <rect x="36" y="16" width="20" height="4"/><rect x="64" y="16" width="20" height="4"/>
        <rect x="36" y="26" width="20" height="4"/><rect x="64" y="26" width="20" height="4"/>
        <rect x="36" y="36" width="20" height="4"/><rect x="64" y="36" width="20" height="4"/>
        <rect x="36" y="46" width="20" height="4"/><rect x="64" y="46" width="20" height="4"/>
        <rect x="36" y="56" width="20" height="4"/><rect x="64" y="56" width="20" height="4"/>
        <rect x="36" y="66" width="20" height="4"/><rect x="64" y="66" width="20" height="4"/>
        <rect x="36" y="76" width="20" height="4"/><rect x="64" y="76" width="20" height="4"/>
        <rect x="36" y="86" width="20" height="4"/><rect x="64" y="86" width="20" height="4"/>
        <rect x="58" y="14" width="4" height="90"/>
      </g>
      <rect x="2" y="104" width="116" height="5" fill="currentColor"/>
      <circle cx="12" cy="88" r="6" fill="currentColor"/><rect x="10" y="88" width="4" height="16" fill="currentColor"/>
      <circle cx="108" cy="88" r="6" fill="currentColor"/><rect x="106" y="88" width="4" height="16" fill="currentColor"/>
    </symbol>

    <symbol id="icon-commercial" viewBox="0 0 120 120">
      <path d="M6 104 V26 Q6 12 32 12 Q54 12 54 24 V104 Z" fill="currentColor"/>
      <g fill="#fff">
        <rect x="12" y="28" width="36" height="4"/><rect x="12" y="38" width="36" height="4"/>
        <rect x="12" y="48" width="36" height="4"/><rect x="12" y="58" width="36" height="4"/>
        <rect x="12" y="68" width="36" height="4"/><rect x="12" y="78" width="36" height="4"/>
        <rect x="12" y="88" width="36" height="4"/>
        <rect x="22" y="24" width="3" height="72"/><rect x="34" y="24" width="3" height="72"/>
      </g>
      <path d="M54 40 L112 52 V104 H54 Z" fill="currentColor"/>
      <g fill="#fff">
        <rect x="62" y="60" width="44" height="4"/><rect x="62" y="70" width="44" height="4"/>
        <rect x="62" y="80" width="44" height="4"/><rect x="76" y="90" width="16" height="14"/>
      </g>
      <rect x="2" y="104" width="116" height="6" fill="currentColor"/>
    </symbol>

    <symbol id="icon-landscape" viewBox="0 0 120 120">
      <circle cx="40" cy="34" r="14" fill="currentColor"/>
      <path d="M2 96 L30 64 L58 96 Z" fill="currentColor"/>
      <path d="M44 96 L80 50 Q84 46 88 50 L118 84 Q122 96 110 96 Z" fill="currentColor"/>
    </symbol>

    <symbol id="icon-concrete" viewBox="0 0 120 120">
      <path d="M8 26 L50 12 V56 L8 52 Z" fill="currentColor"/>
      <rect x="24" y="16" width="4" height="38" fill="#fff"/>
      <rect x="36" y="14" width="4" height="42" fill="#fff"/>
      <rect x="54" y="20" width="10" height="40" fill="currentColor"/>
      <path d="M80 36 H100 L112 56 V82 H80 Z" fill="currentColor"/>
      <rect x="2" y="64" width="78" height="18" fill="currentColor"/>
      <rect x="2" y="82" width="110" height="6" fill="currentColor"/>
      <circle cx="26" cy="90" r="11" fill="#fff"/><circle cx="26" cy="90" r="8" fill="currentColor"/>
      <circle cx="96" cy="90" r="11" fill="#fff"/><circle cx="96" cy="90" r="8" fill="currentColor"/>
    </symbol>

    <symbol id="icon-roller" viewBox="0 0 120 120">
      <rect x="4" y="18" width="6" height="14" fill="currentColor"/>
      <rect x="12" y="8" width="86" height="30" rx="5" fill="currentColor"/>
      <path d="M98 20 H110 V48 L56 62 V74" fill="none" stroke="currentColor" stroke-width="7"/>
      <rect x="46" y="72" width="20" height="40" rx="8" fill="currentColor"/>
    </symbol>

    <symbol id="icon-phone" viewBox="0 0 24 24">
      <circle cx="12" cy="12" r="12" fill="currentColor"/>
      <path d="M8 5.5 L10 9 L8.6 10.4 Q10 13.6 13.6 15.4 L15 14 L18.5 16 L17 18.6 Q10.5 18.5 5.5 8 Z" fill="#253c91"/>
    </symbol>
    <symbol id="icon-pin" viewBox="0 0 24 24">
      <circle cx="12" cy="12" r="12" fill="currentColor"/>
      <path d="M12 5 A5 5 0 0 1 17 10 C17 14 12 19 12 19 C12 19 7 14 7 10 A5 5 0 0 1 12 5 Z" fill="#253c91"/>
      <circle cx="12" cy="10" r="2" fill="currentColor"/>
    </symbol>
    <symbol id="icon-web" viewBox="0 0 24 24">
      <circle cx="12" cy="12" r="12" fill="currentColor"/>
      <g fill="none" stroke="#253c91" stroke-width="1.5">
        <circle cx="12" cy="12" r="7"/>
        <ellipse cx="12" cy="12" rx="3" ry="7"/>
        <path d="M5 12 H19 M6 8.5 H18 M6 15.5 H18"/>
      </g>
    </symbol>
  </defs>
</svg>

<!-- Navy edition -->
<svg class="flyer flyer--navy" viewBox="0 0 1016 1314" role="group" aria-label="Construction services page, navy edition">
  <rect class="paper" x="0" y="0" width="1016" height="1314" fill="#fff"/>
  <rect class="header-panel" x="0" y="0" width="1016" height="220"/>
  <polygon class="photo-area" role="img" aria-label="Photo of a bright white modern building lobby with curved reception desk and glass walls" points="0,213 310,213 413,108 1016,108 1016,634 0,634"/>
  <path class="fine-stripe" d="M0 190 H298 L400 88 H1016"/>
  <path class="accent-stripe" d="M0 206 H306 L409 101 H1016"/>
  <text class="brand-name" x="178" y="118" text-anchor="middle">KARRO</text>
  <text class="city-list" x="947" y="78" text-anchor="end">SYDNEY | CANBERRA | BRISBANE | MELBOURNE</text>

  <path class="heading-rule" d="M380 637 H1016"/>
  <path d="M0 657 H385 Q360 672 380 678 L0 668 Z" fill="url(#tabFade)" opacity="0.7"/>
  <path class="heading-tab" d="M0 590 H372 A33 33 0 0 1 372 657 H0 Z"/>
  <text class="heading-text" x="58" y="638">CONSTRUCTION</text>

  <path class="offer-pill" d="M1016 713 H121 A48 48 0 0 0 121 809 H1016"/>
  <text class="offer-text" x="991" y="753" text-anchor="end">As New Tenants To The Bulding And As A Way Of Introducing Ourselves</text>
  <text class="offer-text" x="991" y="786" text-anchor="end">We Would Like To Offer A <tspan class="offer-strong">10% Discount</tspan> On Any Of The Below Services</text>

  <g class="service">
    <rect class="service-box" x="73" y="864" width="157" height="156" rx="14"/>
    <use class="service-icon" href="#icon-residential" x="92" y="880" width="120" height="120"/>
    <text class="service-label" x="151" y="1054">RESIDENTIAL</text>
    <text class="service-label" x="151" y="1082">BUILDING</text>
  </g>
  <g class="service">
    <rect class="service-box" x="257" y="864" width="157" height="156" rx="14"/>
    <use class="service-icon" href="#icon-commercial" x="276" y="882" width="120" height="120"/>
    <text class="service-label" x="335" y="1054">COMMERCIAL</text>
    <text class="service-label" x="335" y="1082">BUILDING</text>
  </g>
  <g class="service">
    <rect class="service-box" x="441" y="864" width="157" height="156" rx="14"/>
    <use class="service-icon" href="#icon-landscape" x="459" y="885" width="122" height="122"/>
    <text class="service-label" x="520" y="1054">LANDSCAPING</text>
  </g>
  <g class="service">
    <rect class="service-box" x="625" y="864" width="157" height="156" rx="14"/>
    <use class="service-icon" href="#icon-concrete" x="645" y="882" width="118" height="118"/>
    <text class="service-label" x="704" y="1054">CONCRETE</text>
  </g>
  <g class="service">
    <rect class="service-box" x="810" y="864" width="157" height="156" rx="14"/>
    <use class="service-icon" href="#icon-roller" x="833" y="880" width="112" height="112"/>
    <text class="service-label" x="888" y="1054">PAINTING</text>
  </g>

  <line class="footer-rule" x1="0" y1="1126" x2="1016" y2="1126"/>
  <rect class="footer-panel" x="0" y="1129" width="1016" height="185"/>
  <text class="footer-brand" x="172" y="1236" text-anchor="middle">KARRO</text>
  <use class="contact-icon" href="#icon-phone" x="354" y="1165" width="26" height="26"/>
  <text class="contact-line" x="391" y="1187">HOME OFFICE : 1300 22 4810</text>
  <use class="contact-icon" href="#icon-pin" x="354" y="1209" width="26" height="26"/>
  <text class="contact-line" x="391" y="1231">Suite 2.04, 8 Harbour Lane Kellyville</text>
  <use class="contact-icon" href="#icon-web" x="354" y="1253" width="26" height="26"/>
  <text class="contact-line" x="391" y="1276">WWW.KARRO-SERVICES.COM.AU</text>
  <rect class="flyer-edge" x="0" y="0" width="1016" height="1314"/>
</svg>

<!-- Light edition -->
<svg class="flyer flyer--light" viewBox="0 0 1016 1314" role="group" aria-label="Construction services page, light edition">
  <rect class="paper" x="0" y="0" width="1016" height="1314" fill="#fff"/>
  <rect class="header-panel" x="0" y="0" width="1016" height="220"/>
  <polygon class="photo-area" role="img" aria-label="Photo of a bright white modern building lobby with curved reception desk and glass walls" points="0,213 310,213 413,108 1016,108 1016,634 0,634"/>
  <path class="fine-stripe" d="M0 190 H298 L400 88 H1016"/>
  <path class="accent-stripe" d="M0 206 H306 L409 101 H1016"/>
  <text class="brand-name" x="172" y="118" text-anchor="middle">KARRO</text>
  <text class="city-list" x="947" y="78" text-anchor="end">SYDNEY | CANBERRA | BRISBANE | MELBOURNE</text>

  <path class="heading-rule" d="M380 637 H1016"/>
  <path d="M0 657 H385 Q360 672 380 678 L0 668 Z" fill="url(#tabFade)" opacity="0.7"/>
  <path class="heading-tab" d="M0 590 H372 A33 33 0 0 1 372 657 H0 Z"/>
  <text class="heading-text" x="58" y="638">CONSTRUCTION</text>

  <path class="offer-pill" d="M1016 713 H121 A48 48 0 0 0 121 809 H1016 Z"/>
  <text class="offer-text" x="991" y="753" text-anchor="end">As New Tenants To The Bulding And As A Way Of Introducing Ourselves</text>
  <text class="offer-text" x="991" y="786" text-anchor="end">We Would Like To Offer A <tspan class="offer-strong">10% Discount</tspan> On Any Of The Below Services</text>

  <g class="service">
    <rect class="service-box" x="73" y="864" width="157" height="156" rx="14"/>
    <use class="service-icon" href="#icon-residential" x="92" y="880" width="120" height="120"/>
    <text class="service-label" x="151" y="1054">RESIDENTIAL</text>
    <text class="service-label" x="151" y="1082">BUILDING</text>
  </g>
  <g class="service">
    <rect class="service-box" x="257" y="864" width="157" height="156" rx="14"/>
    <use class="service-icon" href="#icon-commercial" x="276" y="882" width="120" height="120"/>
    <text class="service-label" x="335" y="1054">COMMERCIAL</text>
    <text class="service-label" x="335" y="1082">BUILDING</text>
  </g>
  <g class="service">
    <rect class="service-box" x="441" y="864" width="157" height="156" rx="14"/>
    <use class="service-icon" href="#icon-landscape" x="459" y="885" width="122" height="122"/>
    <text class="service-label" x="520" y="1054">LANDSCAPING</text>
  </g>
  <g class="service">
    <rect class="service-box" x="625" y="864" width="157" height="156" rx="14"/>
    <use class="service-icon" href="#icon-concrete" x="645" y="882" width="118" height="118"/>
    <text class="service-label" x="704" y="1054">CONCRETE</text>
  </g>
  <g class="service">
    <rect class="service-box" x="810" y="864" width="157" height="156" rx="14"/>
    <use class="service-icon" href="#icon-roller" x="833" y="880" width="112" height="112"/>
    <text class="service-label" x="888" y="1054">PAINTING</text>
  </g>

  <rect class="footer-panel" x="0" y="1129" width="1016" height="185"/>
  <line class="footer-rule" x1="0" y1="1126" x2="1016" y2="1126"/>
  <text class="footer-brand" x="192" y="1236" text-anchor="middle">KARRO</text>
  <use class="contact-icon" href="#icon-phone" x="339" y="1165" width="26" height="26"/>
  <text class="contact-line" x="376" y="1187">HOME OFFICE : 1300 22 4810</text>
  <use class="contact-icon" href="#icon-pin" x="339" y="1209" width="26" height="26"/>
  <text class="contact-line" x="376" y="1231">Suite 2.04, 8 Harbour Lane Kellyville</text>
  <use class="contact-icon" href="#icon-web" x="339" y="1253" width="26" height="26"/>
  <text class="contact-line" x="376" y="1276">WWW.KARRO-SERVICES.COM.AU</text>
  <rect class="flyer-edge" x="0" y="0" width="1016" height="1314"/>
</svg>

</body>
</html>
```